New Infusion Pharmacy needs Business Card design

Hello!

We are Meridale Infusion Pharmacy, are we are looking for a two sided, clean and modern business card.

First, let me give you a little bit about what an infusion pharmacy does...
We compound and fill prescriptions for drugs that are injectable, meaning that they are administered via an IV bag or a syringe. Basically anything that is too advanced for a normal pill pharmacy to fill. We compound everything in our state of the art clean room, then deliver it directly to the patients home. We have an outside sales force that markets to hospitals, home health agencies, and doctor's offices.

as for the business card...
We are looking for a clean, modern card. our colors are in our logo, kind of a light bule and a darker blue. We do really like the rounded corners on the card. Also, we would like the back of the card to be the reverse colors of the front, for example, if the front of the card has a light background, then the back of the card will have a dark background.

On the back side of the card we want to have our logo, then list some of the services we offer:
-IVIG
-TPN
-Enteral Nutrition
-IV Antibiotics
-IV Hydration
-Blood Factors
-Chemotherapy
-Pain Management

Our logo is uploaded in .psd format, if you need a different format let me know and i'll throw it up here.

Thank you so much!!

Industry/Entity Type

Pharmacy

Requirements
Must have
• Front of Card: (no particular order, please arrange in whatever way you think looks best!)
-Employee Name
-Title
-Office Phone #
-Cell Phone #
-Fax #
-email address - tobin@meridaleinfusion-example.com
-office address - 4127 Harlow St. Brenwick, CA 90612
-Web Site - www.meridaleinfusion-example.com

```html
<!DOCTYPE html>
<html lang="en">
<head>
<meta charset="utf-8">
<title>Meridale Infusion Pharmacy – Business Card</title>
<link rel="stylesheet" href="https://fonts.googleapis.com/css2?family=Arimo:wght@400;700&family=Montserrat:wght@300;400;500;600&display=swap">
<style>
  :root {
    --page-bg: #ecebe8;
    --card-light-top: #ffffff;
    --card-light-edge: #d9dbde;
    --brand-dark: #0d5370;
    --brand-light: #3b9fc6;
    --teal-light: #3a9fc2;
    --teal-dark: #05566e;
    --white: #ffffff;
  }
  * { box-sizing: border-box; margin: 0; padding: 0; }
  html, body { width: 1200px; height: 803px; overflow: hidden; }
  body {
    background: var(--page-bg);
    position: relative;
    font-family: "Arimo", Arial, sans-serif;
  }
  .card {
    position: absolute;
    width: 600px;
    height: 345px;
    border-radius: 14px;
    box-shadow: 0 6px 18px rgba(0,0,0,0.18);
    overflow: hidden;
  }

  /* Services side (light) */
  .card--services {
    left: 60px; top: 50px;
    background: radial-gradient(ellipse at 50% 40%, var(--card-light-top) 0%, #f3f4f5 45%, var(--card-light-edge) 100%);
  }
  .brand {
    position: absolute;
    left: 0; right: 0; top: 108px;
    text-align: center;
    color: var(--brand-dark);
    font-family: "Montserrat", Arial, sans-serif;
  }
  .brand__name { font-size: 50px; font-weight: 500; letter-spacing: 0.5px; line-height: 1; }
  .brand__tagline { font-size: 15px; font-weight: 400; letter-spacing: 4px; margin-top: 6px; }
  .services__rule {
    position: absolute; left: 14px; right: 14px; top: 272px;
    height: 2px; background: var(--brand-dark); opacity: 0.7;
  }
  .services {
    position: absolute; left: 41px; right: 20px; top: 285px;
    display: grid;
    grid-template-columns: 171px 142px 153px auto;
    row-gap: 8px;
    list-style: none;
    color: var(--brand-dark);
    font-size: 14.5px;
    font-weight: 700;
  }

  /* Contact side (dark) */
  .card--contact {
    left: 540px; top: 420px;
    background: linear-gradient(100deg, var(--teal-light) 0%, #1f7f9e 55%, var(--teal-dark) 100%);
    color: var(--white);
  }
  .contact__rule {
    position: absolute; left: 96px; right: 0; top: 100px;
    height: 1.5px; background: var(--white);
  }
  .person { position: absolute; left: 96px; top: 70px; }
  .person__name {
    font-family: "Montserrat", Arial, sans-serif;
    font-weight: 300; font-size: 20px; letter-spacing: 0.5px; line-height: 24px;
  }
  .person__title { font-size: 12.5px; font-weight: 700; margin-top: 14px; }
  .contact-list {
    position: absolute; left: 100px;
    list-style: none;
  }
  .contact-list li { display: flex; align-items: center; gap: 10px; height: 25px; }
  .contact-list svg { width: 16px; height: 16px; fill: var(--white); flex: none; }
  .contact-list--phones { top: 140px; }
  .contact-list--phones li { font-size: 15px; font-weight: 700; }
  .contact-list--web { top: 224px; }
  .contact-list--web li {
    font-family: "Montserrat", Arial, sans-serif; font-weight: 400; font-size: 14px;
  }
</style>
</head>
<body>

<section class="card card--services" aria-label="Card back: services">
  <div class="brand">
    <div class="brand__name">MERIDALE</div>
    <div class="brand__tagline">INFUSION PHARMACY</div>
  </div>
  <div class="services__rule"></div>
  <ul class="services">
    <li>-Chemotherapy</li>
    <li>-IV Hydration</li>
    <li>-Enteral Nutrition</li>
    <li>-IVIG</li>
    <li>-Pain Management</li>
    <li>-Blood Factors</li>
    <li>-IV Antibiotics</li>
    <li>-TPN</li>
  </ul>
</section>

<section class="card card--contact" aria-label="Card front: contact">
  <div class="contact__rule"></div>
  <div class="person">
    <div class="person__name">CORWIN LASTRADE</div>
    <div class="person__title">Sub Director</div>
  </div>
  <ul class="contact-list contact-list--phones">
    <li><svg viewBox="0 0 16 16" aria-hidden="true"><path d="M3 1l3 3-1.5 2a8 8 0 0 0 5.5 5.5L12 10l3 3-2 2C6 15 1 10 1 3z"/></svg>555-014-238</li>
    <li><svg viewBox="0 0 16 16" aria-hidden="true"><path d="M4 0h8a1 1 0 0 1 1 1v14a1 1 0 0 1-1 1H4a1 1 0 0 1-1-1V1a1 1 0 0 1 1-1zm1 2v7h6V2zm1 9v2h1v-2zm3 0v2h1v-2z"/></svg>555-019-774</li>
    <li><svg viewBox="0 0 16 16" aria-hidden="true"><path d="M4 1h6l2 2v3H4zM2 7h12a1 1 0 0 1 1 1v5a1 1 0 0 1-1 1H2a1 1 0 0 1-1-1V8a1 1 0 0 1 1-1zm3 3v2h6v-2z"/></svg>555-01-64</li>
  </ul>
  <ul class="contact-list contact-list--web">
    <li><svg viewBox="0 0 16 16" aria-hidden="true"><path d="M1 3h14v10H1zm1.5 1.2v.3L8 8.6l5.5-4.1v-.3zm0 2v5.6h11V6.2L8 10.3z"/></svg>tobin@meridaleinfusion-example.com</li>
    <li><svg viewBox="0 0 16 16" aria-hidden="true"><path d="M8 0a5 5 0 0 1 5 5c0 4-5 9-5 9S3 9 3 5a5 5 0 0 1 5-5zm0 3a2 2 0 1 0 0 4 2 2 0 0 0 0-4zM4 15h8v1H4z"/></svg>4127 Harlow St. Brenwick, CA 90612</li>
    <li><svg viewBox="0 0 16 16" aria-hidden="true"><path d="M8 1a7 7 0 1 1 0 14A7 7 0 0 1 8 1zm0 1.5a5.5 5.5 0 0 0-3.9 9.4L6 10l-1-2 2-2 2 1 1-2-1-2.4A5.5 5.5 0 0 0 8 2.5zm3 6l-2 2 1 3a5.5 5.5 0 0 0 3-4.5z"/></svg>www.meridaleinfusion-example.com</li>
  </ul>
</section>

</body>
</html>
```